Business Card And Stationary Set for : Pintu Ravel Sdn. Bhd.
I need double sided standard sized Business Card [3.5" x 2"]
Same font or you can recommend
Professional
Ferril Wakin
41C, Jalan Cempaka Lima,
Taman Seroja,
47310 Kuala Lumpur,
Malaysia.
info@pintuvrel.com.my
www.pintuvrel.com.my
618204-K
Please put the company name and license no. above the company address. Smaller font for the license number.
Pintu Ravel Sdn. Bhd. (618204-K)
Company logo.
Specialized In: Auto Gate & Security Systems

```html
<!DOCTYPE html>
<html lang="en">
<head>
<meta charset="utf-8">
<title>Pintu Ravel Sdn. Bhd. – Business Card and Stationery Set</title>
<link rel="stylesheet" href="https://fonts.googleapis.com/css2?family=Arimo:wght@400;700&display=swap">
<style>
  :root{
    --orange:#f7931e;
    --orange-deep:#e8730c;
    --ink:#231f20;
    --charcoal:#3a3a3c;
    --grey:#6d6e71;
    --grey-light:#bcbec0;
    --paper:#ffffff;
    --backdrop:#efeae3;
    --faint:#ececec;
  }
  *{box-sizing:border-box;margin:0;padding:0}
  html,body{width:1200px;height:571px;overflow:hidden;background:var(--backdrop)}
  body{position:relative;font-family:"Arimo",Arial,sans-serif;color:var(--ink)}
  .piece{position:absolute;overflow:hidden;background:var(--paper);box-shadow:0 2px 6px rgba(0,0,0,.18)}
  .piece > svg.shape{position:absolute;inset:0;width:100%;height:100%}
  .brand{position:absolute;display:flex;align-items:center;gap:5px;font-weight:700;letter-spacing:.02em;white-space:nowrap}
  .brand .mark{display:inline-block;background:currentColor}
  .tagline{position:absolute;font-size:6px;color:var(--grey);letter-spacing:.03em;white-space:nowrap}
  .lines{position:absolute;font-size:6px;line-height:1.45;color:var(--grey);white-space:nowrap}
  .lines strong{color:var(--ink)}
  .lines.on-dark{color:#e6e6e6}
  .lines.on-dark strong{color:var(--paper)}
  .person{position:absolute;font-weight:700;white-space:nowrap}
  .role{position:absolute;font-size:6px;white-space:nowrap}
  .dot{display:inline-block;width:4px;height:4px;background:var(--orange);margin-right:3px;vertical-align:middle}
  .watermark{position:absolute;font-weight:700;color:var(--faint);white-space:nowrap;letter-spacing:.04em}

  /* business cards */
  .card{width:204px;height:132px}
  .card-info{left:12px;top:24px}
  .card-contact{left:228px;top:24px;background:var(--ink)}
  .card-logo-white{left:12px;top:173px}
  .card-logo-orange{left:228px;top:173px;background:var(--orange)}
  .card-logo-black{left:132px;top:300px;background:radial-gradient(circle at 50% 45%,#4a4a4c,#161616 75%)}

  /* letterhead */
  .letterhead{left:432px;top:29px;width:336px;height:494px}

  /* envelopes */
  .envelope-back{left:804px;top:29px;width:360px;height:120px}
  .envelope-plain{left:792px;top:132px;width:372px;height:132px}
  .envelope-front{left:667px;top:324px;width:360px;height:228px}
</style>
</head>
<body>

<!-- Business card: details side -->
<section class="piece card card-info" aria-label="Business card, details side">
  <svg class="shape" viewBox="0 0 204 132" preserveAspectRatio="none" aria-hidden="true">
    <path d="M118 0 H204 V132 H100 C128 96 132 40 118 0 Z" fill="var(--grey-light)"/>
    <path d="M124 0 H204 V132 H108 C136 96 138 40 124 0 Z" fill="var(--orange)"/>
  </svg>
  <div class="lines" style="left:9px;top:14px">
    <strong>Pintu Ravel Sdn. Bhd.</strong> (618204-K)<br>
    41C, Jalan Cempaka Lima,<br>
    Taman Seroja,<br>
    47310 Kuala Lumpur,<br>
    Malaysia.
  </div>
  <div class="lines" style="left:9px;top:78px">
    T +603 5512 0834<br>
    F +603 5512 0835<br>
    info@pintuvrel.com.my<br>
    www.pintuvrel.com.my
  </div>
  <div class="person" style="right:10px;top:14px;font-size:9px;color:var(--paper)">Ferril Wakin</div>
  <div class="role" style="right:10px;top:26px;color:var(--paper)">Managing Director</div>
  <div class="lines on-dark" style="right:10px;top:96px;text-align:right">M +6012 384 7719</div>
</section>

<!-- Business card: contact side, dark -->
<section class="piece card card-contact" aria-label="Business card, contact side">
  <svg class="shape" viewBox="0 0 204 132" preserveAspectRatio="none" aria-hidden="true">
    <path d="M0 0 H92 C110 40 110 92 92 132 H0 Z" fill="var(--orange)"/>
    <path d="M0 0 H86 C104 40 104 92 86 132 H0 Z" fill="var(--paper)"/>
  </svg>
  <div class="brand" style="left:8px;top:52px;font-size:11px;color:var(--ink)"><span class="mark" style="width:9px;height:9px"></span>PINTU RAVEL</div>
  <div class="tagline" style="left:22px;top:66px;font-size:4.5px">Auto Gate &amp; Security Systems</div>
  <div class="person" style="right:9px;top:10px;font-size:9px;color:var(--paper)">Ferril Wakin</div>
  <div class="role" style="right:9px;top:21px;color:var(--orange)">Managing Director</div>
  <div class="lines on-dark" style="left:104px;top:50px">
    <span class="dot"></span>T +603 5512 0834<br>
    <span class="dot"></span>F +603 5512 0835<br>
    <span class="dot"></span>M +6012 384 7719<br>
    <span class="dot"></span>info@pintuvrel.com.my<br>
    <span class="dot"></span>www.pintuvrel.com.my
  </div>
</section>

<!-- Business card: brand side, white -->
<section class="piece card card-logo-white" aria-label="Business card, brand side on white">
  <svg class="shape" viewBox="0 0 204 132" preserveAspectRatio="none" aria-hidden="true">
    <path d="M0 0 H14 C4 44 4 88 14 132 H0 Z" fill="var(--orange)"/>
  </svg>
  <div class="brand" style="left:50%;top:58px;transform:translateX(-50%);font-size:13px;color:var(--ink)"><span class="mark" style="width:11px;height:11px"></span>PINTU RAVEL</div>
</section>

<!-- Business card: brand side, orange -->
<section class="piece card card-logo-orange" aria-label="Business card, brand side on orange">
  <div class="brand" style="left:50%;top:58px;transform:translateX(-50%);font-size:13px;color:var(--ink)"><span class="mark" style="width:11px;height:11px"></span>PINTU RAVEL</div>
</section>

<!-- Business card: brand side, black -->
<section class="piece card card-logo-black" aria-label="Business card, brand side on black">
  <div class="brand" style="left:50%;top:56px;transform:translateX(-50%);font-size:13px;color:var(--paper)"><span class="mark" style="width:11px;height:11px;background:var(--orange)"></span>PINTU RAVEL</div>
</section>

<!-- Letterhead -->
<section class="piece letterhead" aria-label="Letterhead">
  <svg class="shape" viewBox="0 0 336 494" preserveAspectRatio="none" aria-hidden="true">
    <path d="M0 0 H18 C6 160 6 330 22 494 H0 Z" fill="var(--orange)"/>
    <path d="M30 494 C120 462 230 456 336 470 V494 Z" fill="var(--grey-light)"/>
    <path d="M0 494 C30 470 60 462 90 460 C50 470 30 482 22 494 Z" fill="var(--orange-deep)"/>
  </svg>
  <div class="brand" style="left:30px;top:20px;font-size:15px;color:var(--ink)"><span class="mark" style="width:12px;height:12px;background:var(--orange)"></span>PINTU RAVEL</div>
  <div class="tagline" style="left:47px;top:40px">Auto Gate &amp; Security Systems</div>
  <div class="lines" style="left:180px;top:18px;font-size:5.5px">
    <strong>Pintu Ravel Sdn. Bhd.</strong> (618204-K)<br>
    41C, Jalan Cempaka Lima, Taman Seroja,<br>
    47310 Kuala Lumpur, Malaysia.<br>
    <span class="dot"></span>T +603 5512 0834<br>
    <span class="dot"></span>F +603 5512 0835<br>
    <span class="dot"></span>info@pintuvrel.com.my
  </div>
  <div class="watermark" style="left:50%;top:240px;transform:translateX(-50%);font-size:30px">PINTU RAVEL</div>
</section>

<!-- Envelope, back with grey flap -->
<section class="piece envelope-back" aria-label="Envelope, back">
  <svg class="shape" viewBox="0 0 360 120" preserveAspectRatio="none" aria-hidden="true">
    <path d="M0 0 H360 L200 84 Q180 94 160 84 Z" fill="var(--grey)"/>
    <path d="M0 120 L150 64 M360 120 L210 64" stroke="#e0e0e0" stroke-width="1" fill="none"/>
  </svg>
  <div class="brand" style="left:50%;top:34px;transform:translateX(-50%);font-size:11px;color:var(--paper)"><span class="mark" style="width:9px;height:9px;background:var(--orange)"></span>PINTU RAVEL</div>
</section>

<!-- Envelope, plain white -->
<section class="piece envelope-plain" aria-label="Envelope, plain back">
  <svg class="shape" viewBox="0 0 372 132" preserveAspectRatio="none" aria-hidden="true">
    <path d="M0 0 L186 70 L372 0" stroke="#e4e4e4" stroke-width="1" fill="none"/>
    <path d="M0 132 L160 60 M372 132 L212 60" stroke="#ededed" stroke-width="1" fill="none"/>
  </svg>
</section>

<!-- Envelope, front -->
<section class="piece envelope-front" aria-label="Envelope, front">
  <svg class="shape" viewBox="0 0 360 228" preserveAspectRatio="none" aria-hidden="true">
    <path d="M0 0 H360 V30 C250 66 110 60 0 28 Z" fill="var(--grey-light)"/>
    <path d="M0 0 H360 V24 C250 58 110 54 0 22 Z" fill="var(--orange)"/>
  </svg>
  <div class="brand" style="left:14px;top:64px;font-size:13px;color:var(--ink)"><span class="mark" style="width:11px;height:11px;background:var(--orange)"></span>PINTU RAVEL</div>
  <div class="tagline" style="left:30px;top:82px">Auto Gate &amp; Security Systems</div>
  <div class="lines" style="left:14px;top:150px;font-size:5.5px">
    <strong>Pintu Ravel Sdn. Bhd.</strong> (618204-K)<br>
    41C, Jalan Cempaka Lima, Taman Seroja,<br>
    47310 Kuala Lumpur, Malaysia.<br>
    <span class="dot"></span>T +603 5512 0834<br>
    <span class="dot"></span>F +603 5512 0835<br>
    <span class="dot"></span>www.pintuvrel.com.my
  </div>
  <div class="watermark" style="right:16px;top:150px;font-size:20px">PINTU RAVEL</div>
</section>

</body>
</html>
```